Business cards and stationery for small forestry/oilfield consulting company
Pine Ledger Consulting Ltd
Business cards and stationery for small forestry/oilfield consulting company - Environment
Creative Brief
Professional
K.J. Dorrin Waltby
RPFT
Box 42 Site 7 RR5 Alberta, Canada T0X 9Q7
pineledger@quorvanet.ca
The name of Pine Ledger Consulting Ltd is in the logo itself, not needed to repeat unless somehow artistically beneficial
Concepts
Business Cards, Letterhead, and Envelopes

```html
<!DOCTYPE html>
<html lang="en">
<head>
<meta charset="utf-8">
<title>Pine Ledger Consulting Ltd – Business Card</title>
<link href="https://fonts.googleapis.com/css2?family=Cinzel:wght@400;600&family=Cormorant+Garamond:ital,wght@0,500;1,500&family=Lato:wght@400&display=swap" rel="stylesheet">
<style>
  :root {
    --bg: #e9eaea;
    --paper: #ffffff;
    --green-deep: #0f5a48;
    --green: #1a7a62;
    --green-light: #3f9a80;
    --ink: #3b3f3e;
    --white: #ffffff;
  }
  * { box-sizing: border-box; margin: 0; padding: 0; }
  html, body { width: 1200px; height: 980px; overflow: hidden; }
  body {
    background: var(--bg);
    display: flex;
    flex-direction: column;
    align-items: center;
    justify-content: center;
    gap: 60px;
    font-family: "Lato", sans-serif;
  }
  .card {
    position: relative;
    width: 640px;
    height: 366px;
    border-radius: 22px;
    overflow: hidden;
    box-shadow: 0 6px 18px rgba(0,0,0,0.18);
  }
  /* Front */
  .card-front { background: var(--paper); }
  .card-front .wave { position: absolute; inset: 0; }
  .brand { position: absolute; left: 44px; top: 30px; }
  .brand-name {
    font-family: "Cinzel", serif;
    font-weight: 600;
    font-size: 40px;
    letter-spacing: 2px;
    color: var(--ink);
    line-height: 1;
  }
  .brand-tag {
    font-family: "Cinzel", serif;
    font-weight: 400;
    font-size: 17px;
    letter-spacing: 6px;
    color: var(--green);
    margin-top: 6px;
  }
  .contact-list {
    position: absolute;
    left: 44px;
    top: 112px;
    list-style: none;
    font-size: 11px;
    color: var(--ink);
    line-height: 15px;
  }
  .contact-list li { display: flex; align-items: center; gap: 8px; }
  .contact-list .dot {
    width: 8px; height: 8px; border-radius: 50%;
    background: var(--green); flex: none;
  }
  .holder {
    position: absolute;
    right: 36px;
    bottom: 22px;
    text-align: right;
    color: var(--white);
    font-family: "Cormorant Garamond", serif;
  }
  .holder-name { font-size: 19px; font-style: italic; letter-spacing: 1px; }
  .holder-title { font-size: 11px; letter-spacing: 2px; font-style: normal; }
  /* Back */
  .card-back {
    background: radial-gradient(ellipse at 50% 40%, var(--green) 0%, var(--green-deep) 85%);
    display: flex;
    flex-direction: column;
    align-items: center;
    justify-content: center;
    color: var(--white);
  }
  .card-back .brand-name { color: var(--white); font-size: 36px; }
  .card-back .web {
    margin-top: 22px;
    font-family: "Cormorant Garamond", serif;
    font-size: 14px;
    letter-spacing: 6px;
  }
</style>
</head>
<body>
  <section class="card card-front">
    <svg class="wave" viewBox="0 0 640 366" preserveAspectRatio="none" aria-hidden="true">
      <path d="M0 262 C170 230 330 325 640 238 L640 366 L0 366 Z" fill="var(--green-light)"/>
      <path d="M0 273 C170 246 330 337 640 252 L640 366 L0 366 Z" fill="var(--white)"/>
      <path d="M0 282 C180 254 340 348 640 264 L640 366 L0 366 Z" fill="var(--green)"/>
      <path d="M0 306 C200 278 360 362 640 296 L640 366 L0 366 Z" fill="var(--green-deep)" opacity="0.55"/>
    </svg>
    <div class="brand">
      <div class="brand-name">PINE LEDGER</div>
      <div class="brand-tag">CONSULTING LTD</div>
    </div>
    <ul class="contact-list">
      <li><span class="dot"></span>Box 42 Site 7 RR5</li>
      <li><span class="dot"></span>Alberta, Canada T0X 9Q7</li>
      <li><span class="dot"></span>403-555-0147</li>
      <li><span class="dot"></span>403-555-0182</li>
      <li><span class="dot"></span>pineledger@quorvanet.ca</li>
      <li><span class="dot"></span>Marvo83</li>
      <li><span class="dot"></span>www.quorvanet.ca</li>
    </ul>
    <div class="holder">
      <div class="holder-name">K.J. Dorrin Waltby</div>
      <div class="holder-title">RPFT</div>
    </div>
  </section>

  <section class="card card-back">
    <div class="brand-name">PINE LEDGER</div>
    <div class="web">WWW.QUORVANET.CA</div>
  </section>
</body>
</html>
```